Business Card Design

Provide project management services to the construction and other industries
Construction services - Civil and Concrete works
Shop Detailing
Structural Modelling
Client side coordination of project teams and consultants
Feasibility Studies for construction projects

Industry/Entity Type

Business

Contact Information for Business Card

Plan Sure
Derek Calloway B.Eng (Hons), G.C.Bus.
Director

m: 0412 738 564
e: dcalloway@plansure.com.au

p: 08 6358 2714
a: 17 Banksia Court, Stirling, WA 6021

```html
<!DOCTYPE html>
<html lang="en">
<head>
<meta charset="utf-8">
<title>Plan Sure – Business Card</title>
<link href="https://fonts.googleapis.com/css2?family=Arimo:wght@400;700&display=swap" rel="stylesheet">
<style>
  :root {
    --page-bg: #ffffff;
    --card-light: #ffffff;
    --card-dark: #0a0b0d;
    --ink: #000000;
    --brand-green: #13803f;
    --rule-grey: #6e6e6e;
    --rule-dark: #1a1a1a;
    --rule-light: #ffffff;
    --rule-muted: #8a8a8a;
  }
  * { margin: 0; padding: 0; box-sizing: border-box; }
  html, body {
    width: 1200px;
    height: 1000px;
    overflow: hidden;
    background: var(--page-bg);
    font-family: "Arimo", Arial, sans-serif;
  }
  .canvas { position: relative; width: 1200px; height: 1000px; }

  .card {
    position: absolute;
    top: 369px;
    width: 454px;
    height: 265px;
    box-shadow: 2px 3px 7px rgba(0,0,0,0.35);
  }
  .card--front { left: 134px; background: var(--card-light); }
  .card--back  { left: 612px; background: var(--card-dark); }

  .wordmark {
    position: absolute;
    font-weight: 700;
    font-size: 30px;
    letter-spacing: 0.5px;
    line-height: 1;
    text-transform: uppercase;
    white-space: nowrap;
  }
  .card--front .wordmark { right: 17px; top: 56px; color: var(--ink); }
  .card--back .wordmark {
    left: 0; right: 0; top: 116px;
    text-align: center; color: #ffffff;
  }

  .rule { position: absolute; left: 18px; right: 18px; height: 1px; }
  .card--front .rule--top { top: 106px; background: var(--rule-grey); }
  .card--front .rule--bottom { top: 157px; background: var(--rule-dark); }
  .card--back .rule--top { top: 106px; background: var(--rule-muted); }
  .card--back .rule--bottom { top: 157px; background: var(--rule-light); }

  .person { position: absolute; left: 40px; top: 115px; }
  .person__name { font-weight: 700; font-size: 15px; color: var(--ink); line-height: 19px; }
  .person__title { font-size: 14px; color: var(--brand-green); line-height: 17px; }

  .contact {
    position: absolute;
    left: 40px;
    top: 176px;
    list-style: none;
    font-size: 14px;
    line-height: 17.7px;
    color: var(--ink);
  }
  .contact__row { display: flex; }
  .contact__label {
    width: 26px;
    font-weight: 700;
    color: var(--brand-green);
  }
</style>
</head>
<body>
<main class="canvas">
  <section class="card card--front" aria-label="Business card front">
    <div class="wordmark">Plan Sure</div>
    <div class="rule rule--top"></div>
    <div class="person">
      <p class="person__name">Derek Calloway B.Eng (Hons), G.C.Bus.</p>
      <p class="person__title">Director</p>
    </div>
    <div class="rule rule--bottom"></div>
    <ul class="contact">
      <li class="contact__row"><span class="contact__label">p</span><span>08 6358 2714</span></li>
      <li class="contact__row"><span class="contact__label">m</span><span>0412 738 564</span></li>
      <li class="contact__row"><span class="contact__label">e</span><span>dcalloway@plansure.com.au</span></li>
      <li class="contact__row"><span class="contact__label">a</span><span>17 Banksia Court, Stirling, WA 6021</span></li>
    </ul>
  </section>

  <section class="card card--back" aria-label="Business card back">
    <div class="rule rule--top"></div>
    <div class="wordmark">Plan Sure</div>
    <div class="rule rule--bottom"></div>
  </section>
</main>
</body>
</html>
```